BrivaTrek Freight Services Business cards

Would like a very unique design catchy but professional for business cards. Please use log provided.Marlon WellsCeo and Founder TransCon Logistix Solutions1-888-913-3225mwells@tlsolutionsus.comwww.bfservicesco.com

```html
<!DOCTYPE html>
<html lang="en">
<head>
<meta charset="utf-8">
<title>BrivaTrek Freight Services – Business Cards</title>
<link rel="stylesheet" href="https://fonts.googleapis.com/css2?family=Lato:wght@400;700&display=swap">
<style>
  :root {
    --bg: #4b3a2f;
    --red: #ec1c24;
    --blue: #1a73bf;
    --navy: #0d2a4a;
    --white: #ffffff;
    --name-blue: #1f6fb5;
  }
  * { margin: 0; padding: 0; box-sizing: border-box; }
  html, body { width: 1200px; height: 960px; overflow: hidden; }
  body {
    background: var(--bg);
    font-family: "Lato", Arial, sans-serif;
    position: relative;
  }
  .card {
    position: absolute;
    border-radius: 30px;
    overflow: hidden;
    box-shadow: 0 6px 14px rgba(0,0,0,0.45);
  }
  .card-front {
    left: 237px; top: 47px; width: 721px; height: 405px;
    background: var(--red);
    color: var(--white);
    text-align: center;
  }
  .front-brand {
    position: absolute; left: 0; right: 0; top: 128px;
    font-size: 50px; font-weight: 700; letter-spacing: 0.5px;
  }
  .front-web {
    position: absolute; left: 0; right: 0; top: 300px;
    font-size: 19px; letter-spacing: 3px; font-weight: 700;
  }
  .card-back {
    left: 244px; top: 507px; width: 706px; height: 407px;
    background: var(--white);
  }
  .back-shapes { position: absolute; inset: 0; }
  .back-brand {
    position: absolute; left: 38px; top: 70px;
    display: flex; align-items: center; gap: 12px;
    color: var(--blue); font-size: 27px; font-weight: 700;
  }
  .brand-square { width: 22px; height: 22px; background: var(--red); }
  .person { position: absolute; left: 36px; top: 235px; }
  .person-name { color: var(--name-blue); font-size: 23px; font-weight: 700; }
  .person-title { color: var(--red); font-size: 18px; margin-top: 6px; }
  .contacts {
    position: absolute; right: 20px; top: 253px;
    color: var(--white); font-size: 16px; text-align: right;
  }
  .contact-line {
    display: flex; align-items: center; justify-content: flex-end;
    gap: 8px; height: 30px;
  }
  .contact-line svg { width: 15px; height: 15px; }
  .address {
    position: absolute; right: 22px; top: 357px;
    color: var(--white); font-size: 16.5px;
  }
</style>
</head>
<body>
  <section class="card card-front">
    <div class="front-brand">BrivaTrek Freight Services</div>
    <div class="front-web">www.<b>bfservicesco</b>.com</div>
  </section>

  <section class="card card-back">
    <svg class="back-shapes" viewBox="0 0 706 407" width="706" height="407">
      <path d="M706,18 C640,140 500,265 0,338 L0,407 L706,407 Z" fill="var(--blue)"/>
      <path d="M0,300 C160,348 360,300 497,224 C360,330 170,362 0,346 Z" fill="var(--navy)"/>
      <path d="M0,328 C170,356 360,318 497,224 C380,320 180,352 0,336 Z" fill="var(--white)"/>
    </svg>

    <div class="back-brand"><span class="brand-square"></span>BrivaTrek Freight Services</div>

    <div class="person">
      <div class="person-name">DUSTIN HARROW</div>
      <div class="person-title">CEO AND FOUNDER</div>
    </div>

    <div class="contacts">
      <div class="contact-line">1-888-472-6081
        <svg viewBox="0 0 16 16"><circle cx="8" cy="8" r="7" fill="none" stroke="#fff" stroke-width="1.3"/><path d="M5.5,4.5 L7,6 L6.2,7.2 C6.8,8.5 7.6,9.3 8.8,9.8 L10,9 L11.5,10.5 L10.5,11.6 C7.5,11.2 4.8,8.5 4.4,5.5 Z" fill="#fff"/></svg>
      </div>
      <div class="contact-line">dharrow@bfservicesco.com
        <svg viewBox="0 0 16 16"><rect x="1.5" y="4" width="13" height="9" rx="1" fill="#fff"/><path d="M1.5,4.5 L8,9 L14.5,4.5" fill="none" stroke="var(--blue)" stroke-width="1.2"/></svg>
      </div>
      <div class="contact-line">www.bfservicesco.com
        <svg viewBox="0 0 16 16"><circle cx="8" cy="8" r="6.5" fill="none" stroke="#fff" stroke-width="1.2"/><ellipse cx="8" cy="8" rx="3" ry="6.5" fill="none" stroke="#fff" stroke-width="1"/><path d="M1.5,8 H14.5 M2.5,5 H13.5 M2.5,11 H13.5" stroke="#fff" stroke-width="1"/></svg>
      </div>
    </div>

    <div class="address">2417 Larkmoor Ave, Atlanta, GA 30318</div>
  </section>
</body>
</html>
```